Granite Ridge Holdings

I have a real estate investment business.

** I need editable vector files of the final design.

Industry/Entity Type

Real Estate

Contact Information for Business Card

I would like the card to be clear and direct with the company name and contact info. I would prefer not to have a design that is too busy (i.e., with excessive detail) in the business card.

Font styles to use
Sans Serif

Requirements
Must have
• My card must have the following information listed below:
• Company name: Grainite Ridge Holdings LLC
• My name: Daniel Vorsley
• Phone number: (555) 218-9067
• Email address: dtvorsley@mailbox-example.net
• Keywords: “Real Estate Investments”
Nice to have
• I would like to have a design that resembles the characteristics/uses of obsidian stone which resembles something related to strength and resilience. Perhaps something with sharp, sleek color transitions as well.

```html
<!DOCTYPE html>
<html lang="en">
<head>
<meta charset="utf-8">
<title>Grainite Ridge Holdings LLC – Business Card</title>
<link rel="stylesheet" href="https://fonts.googleapis.com/css2?family=Oswald:wght@500&family=Josefin+Sans:wght@400;600&display=swap">
<style>
  :root {
    --page-bg: #2b2d30;
    --card-bg: #ffffff;
    --blue-light: #3b80bd;
    --blue-dark: #1c4a7a;
    --navy-text: #1d4a80;
    --ink: #151515;
    --panel-dark-1: #2a2c2f;
    --panel-dark-2: #111214;
  }
  * { box-sizing: border-box; margin: 0; padding: 0; }
  html, body { width: 1200px; height: 1200px; overflow: hidden; }
  body {
    background: var(--page-bg);
    position: relative;
    font-family: "Josefin Sans", sans-serif;
  }
  .card {
    position: absolute;
    left: 150px;
    width: 900px;
    height: 550px;
    background: var(--card-bg);
    overflow: hidden;
  }
  .card--front { top: 30px; }
  .card--back { top: 620px; }

  .stripes { position: absolute; display: block; }
  .stripes--top-left { left: 0; top: 0; width: 323px; height: 87px; }
  .stripes--bottom-right { right: 0; bottom: 0; width: 325px; height: 88px; }

  .brand-mark {
    position: absolute;
    width: 64px; height: 64px;
    left: 50%;
    transform: translateX(-50%);
    background: var(--navy-text);
  }
  .card--front .brand-mark { top: 150px; }

  .company-name {
    position: absolute;
    left: 0; right: 0;
    text-align: center;
    font-family: "Oswald", sans-serif;
    font-weight: 500;
    text-transform: uppercase;
    line-height: 1;
  }
  .card--front .company-name {
    top: 262px;
    color: var(--navy-text);
    font-size: 58px;
    letter-spacing: 11px;
  }
  .company-name span { display: block; margin-bottom: 20px; }

  .back-panel {
    position: absolute;
    left: 0; top: 0;
    width: 409px; height: 550px;
    display: block;
  }
  .panel-scene {
    position: absolute;
    left: 0; top: 61px;
    width: 409px; height: 198px;
    background: linear-gradient(180deg, var(--panel-dark-1) 0%, var(--panel-dark-2) 100%);
  }
  .panel-scene .brand-mark {
    top: 22px;
    width: 50px; height: 50px;
    background: #ffffff;
  }
  .panel-scene .company-name {
    top: 96px;
    color: #ffffff;
    font-size: 34px;
    letter-spacing: 5px;
  }
  .panel-scene .company-name span { margin-bottom: 14px; }

  .contact-rail { position: absolute; left: 430px; top: 0; width: 60px; height: 550px; }

  .person-name {
    position: absolute;
    left: 503px; top: 120px;
    font-family: "Oswald", sans-serif;
    font-weight: 500;
    font-size: 42px;
    letter-spacing: 6px;
    color: var(--ink);
    line-height: 1;
  }
  .person-name .surname { color: var(--navy-text); margin-left: 14px; }
  .person-role {
    position: absolute;
    left: 504px; top: 176px;
    font-weight: 600;
    font-size: 17px;
    letter-spacing: 2.6px;
    color: var(--ink);
  }
  .contact-line {
    position: absolute;
    left: 503px;
    font-size: 25px;
    letter-spacing: 4px;
    color: var(--ink);
  }
  .contact-line--phone { top: 288px; }
  .contact-line--email { top: 444px; font-size: 20px; letter-spacing: 1.6px; }
</style>
</head>
<body>

<section class="card card--front" aria-label="Business card front">
  <svg class="stripes stripes--top-left" viewBox="0 0 323 87" aria-hidden="true">
    <polygon points="0,0 288,0 323,19 0,19" fill="var(--blue-dark)"/>
    <rect x="0" y="19" width="323" height="24" fill="var(--blue-light)"/>
    <polygon points="0,43 288,43 323,63 0,63" fill="var(--blue-dark)"/>
    <rect x="0" y="63" width="323" height="24" fill="var(--blue-light)"/>
  </svg>

  <div class="brand-mark" aria-hidden="true"></div>
  <h1 class="company-name"><span>Grainite Ridge</span><span>Holdings LLC</span></h1>

  <svg class="stripes stripes--bottom-right" viewBox="0 0 325 88" aria-hidden="true">
    <rect x="0" y="0" width="325" height="23" fill="var(--blue-light)"/>
    <polygon points="0,23 325,23 325,43 35,43" fill="var(--blue-dark)"/>
    <rect x="0" y="43" width="325" height="24" fill="var(--blue-light)"/>
    <polygon points="0,67 325,67 325,88 35,88" fill="var(--blue-dark)"/>
  </svg>
</section>

<section class="card card--back" aria-label="Business card back">
  <svg class="back-panel" viewBox="0 0 409 550" aria-hidden="true">
    <rect x="0" y="0" width="409" height="550" fill="var(--blue-light)"/>
    <polygon points="0,321 409,321 372,361 0,361" fill="var(--blue-dark)"/>
    <polygon points="0,422 409,422 376,459 0,459" fill="var(--blue-dark)"/>
  </svg>

  <div class="panel-scene" role="img" aria-label="Dark city skyline photograph behind the company name">
    <div class="brand-mark" aria-hidden="true"></div>
    <p class="company-name"><span>Grainite Ridge</span><span>Holdings LLC</span></p>
  </div>

  <svg class="contact-rail" viewBox="0 0 60 550" aria-hidden="true">
    <line x1="28" y1="0" x2="28" y2="550" stroke="#222" stroke-width="1.5"/>
    <line x1="33" y1="0" x2="33" y2="550" stroke="#222" stroke-width="1.5"/>
    <circle cx="30" cy="300" r="24" fill="#111"/>
    <path d="M20 291 q2 -4 6 -3 l3 6 q0 2 -3 3 q2 6 8 9 q1 -3 3 -3 l6 3 q1 4 -3 6 q-12 0 -20 -21z" fill="#fff"/>
    <path d="M33 289 a9 9 0 0 1 8 8" stroke="#fff" stroke-width="2" fill="none"/>
    <circle cx="30" cy="453" r="24" fill="#111"/>
    <rect x="18" y="444" width="24" height="18" rx="3" fill="none" stroke="#fff" stroke-width="2.5"/>
    <polyline points="19,446 30,455 41,446" fill="none" stroke="#fff" stroke-width="2.5"/>
  </svg>

  <h2 class="person-name">Daniel<span class="surname">VORSLEY</span></h2>
  <p class="person-role">Real Estate Investments</p>
  <p class="contact-line contact-line--phone">(555)2189067</p>
  <p class="contact-line contact-line--email">dtvorsley@mailbox-example.net</p>
</section>

</body>
</html>
```